Evaporative Air Conditioning Summer Service

Would like to design a flyer to send out in an email to existing clients to promote a Pre-summer service for Evaporative Air Conditioners
Cost will be $110.00 inc gst
Tasks included in service are
- Inspection and clean of pads
- Inspection and check float valve, water pump, fan, motor, bearings, drain
- Clean basin
- Supply of bacterial tablet
- Inspect overall condition of unit
- Any repairs if required will be quoted
Please see files attached of a previous very basic flyer I have used for installation and replacement unit costs. This has current contact information
Have also uploaded company logo for use.
Thanks

```html
<!DOCTYPE html>
<html lang="en">
<head>
<meta charset="utf-8">
<title>Pre-summer Service for Evaporative Air Conditioners</title>
<link rel="stylesheet" href="https://fonts.googleapis.com/css2?family=Sora:wght@600;700&family=Poppins:wght@400;600&display=swap">
<style>
  :root {
    --navy: #1f3263;
    --navy-deep: #1a2a55;
    --cream: #fbeecb;
    --orange: #f08a24;
    --orange-red: #e8542a;
    --yellow: #f9b233;
    --text: #2b2b2b;
    --white: #ffffff;
  }
  * { box-sizing: border-box; margin: 0; padding: 0; }
  html, body { width: 848px; height: 1200px; overflow: hidden; background: var(--white); }
  .flyer {
    position: relative;
    width: 848px;
    height: 1200px;
    overflow: hidden;
    background: var(--white);
    font-family: "Poppins", Arial, sans-serif;
    color: var(--text);
  }
  .backdrop { position: absolute; inset: 0; }
  .brand {
    position: absolute;
    left: 58px;
    top: 60px;
    display: flex;
    align-items: center;
    gap: 10px;
  }
  .brand-dot {
    width: 34px; height: 34px;
    border-radius: 50%;
    background: var(--navy);
  }
  .brand-name {
    font-family: "Sora", sans-serif;
    font-weight: 700;
    font-size: 22px;
    line-height: 1.05;
    color: var(--navy);
  }
  .headline {
    position: absolute;
    left: 50px;
    top: 722px;
    font-family: "Sora", sans-serif;
    font-weight: 600;
    font-size: 43px;
    line-height: 1.2;
    color: var(--navy);
    letter-spacing: -0.5px;
  }
  .tasks {
    position: absolute;
    left: 44px;
    list-style: none;
    font-size: 18.5px;
    line-height: 21px;
    color: var(--text);
    white-space: nowrap;
  }
  .tasks li::before {
    content: "";
    display: inline-block;
    width: 6px; height: 6px;
    border-radius: 50%;
    background: var(--text);
    margin: 0 9px 4px 2px;
  }
  .tasks--top { top: 840px; }
  .tasks--bottom { top: 973px; line-height: 22px; }
  .parts {
    position: absolute;
    left: 54px;
    top: 893px;
    display: flex;
    gap: 51px;
  }
  .part {
    width: 72px; height: 68px;
    border: 1.5px solid var(--orange);
    background: linear-gradient(160deg, #f4f5f7, #cfd3da);
  }
  .price {
    position: absolute;
    right: 52px;
    top: 990px;
    text-align: right;
    font-family: "Sora", sans-serif;
    font-weight: 700;
    font-size: 34px;
    line-height: 1;
    color: var(--navy);
  }
  .price small {
    display: block;
    margin-top: 6px;
    font-family: "Poppins", Arial, sans-serif;
    font-weight: 600;
    font-size: 15px;
    color: var(--orange-red);
  }
  .footer {
    position: absolute;
    left: 0; bottom: 0;
    width: 848px;
    padding: 0 0 8px 30px;
    color: var(--white);
    font-size: 12.5px;
    line-height: 20px;
  }
  .contact { display: flex; align-items: center; gap: 8px; }
  .contact svg { width: 15px; height: 15px; fill: var(--white); }
</style>
</head>
<body>
<div class="flyer">
  <svg class="backdrop" width="848" height="1200" viewBox="0 0 848 1200" aria-hidden="true">
    <defs>
      <linearGradient id="skyBlue" x1="0" y1="0" x2="1" y2="1">
        <stop offset="0" stop-color="#6e8fd0"/>
        <stop offset="1" stop-color="#4a67b0"/>
      </linearGradient>
      <linearGradient id="bandOrange" x1="0" y1="1" x2="1" y2="0">
        <stop offset="0" stop-color="#f9b233"/>
        <stop offset="0.5" stop-color="#f08a24"/>
        <stop offset="1" stop-color="#e8542a"/>
      </linearGradient>
      <linearGradient id="footerBand" x1="0" y1="0" x2="1" y2="0">
        <stop offset="0" stop-color="#e8542a"/>
        <stop offset="1" stop-color="#f08a24"/>
      </linearGradient>
    </defs>
    <path d="M0 150 C150 120 300 240 330 420 C360 600 300 700 200 720 L0 720 Z" fill="var(--cream)"/>
    <path d="M300 0 L848 0 L848 560 C700 560 520 520 420 420 C300 300 180 180 300 0 Z" fill="url(#skyBlue)"/>
    <g role="img" aria-label="Photo of a rooftop evaporative air conditioning unit against a blue sky">
      <path d="M270 330 C290 150 440 90 600 100 C740 110 848 170 848 200 L848 470 C760 560 640 640 500 650 C360 650 255 500 270 330 Z" fill="#8c96a3"/>
      <path d="M270 330 C290 150 440 90 600 100 C740 110 848 170 848 200 L848 260 C700 250 450 240 272 300 Z" fill="#7d98d2"/>
    </g>
    <circle cx="728" cy="662" r="66" fill="var(--navy)"/>
    <path d="M410 640 C560 700 720 640 848 460 L848 560 C740 700 560 760 410 640 Z" fill="url(#bandOrange)"/>
    <path d="M0 1068 C250 1066 560 1078 848 1040 L848 1200 L0 1200 Z" fill="url(#footerBand)"/>
    <path d="M0 1098 C280 1086 560 1100 848 1076 L848 1200 L0 1200 Z" fill="var(--navy-deep)"/>
  </svg>

  <div class="brand">
    <span class="brand-dot"></span>
    <span class="brand-name">HARBOURLINE<br>Gas &amp; Plumbing</span>
  </div>

  <h1 class="headline">Pre-summer service for<br>Evaporative Air Conditioners</h1>

  <ul class="tasks tasks--top">
    <li>Inspection and clean of pads</li>
    <li>Inspection and check float valve, water pump, fan, motor, bearings, drain</li>
  </ul>

  <div class="parts">
    <div class="part" role="img" aria-label="Float valve"></div>
    <div class="part" role="img" aria-label="Water pump"></div>
    <div class="part" role="img" aria-label="Fan"></div>
    <div class="part" role="img" aria-label="Motor"></div>
    <div class="part" role="img" aria-label="Bearings"></div>
    <div class="part" role="img" aria-label="Drain"></div>
  </div>

  <ul class="tasks tasks--bottom">
    <li>Clean basin</li>
    <li>Supply of bacterial tablet</li>
    <li>Inspect overall condition of unit</li>
    <li>Any repairs if required will be quoted</li>
  </ul>

  <div class="price">$110.00<small>inc GST</small></div>

  <div class="footer">
    <div class="contact">
      <svg viewBox="0 0 24 24"><path d="M6.6 10.8a15.1 15.1 0 0 0 6.6 6.6l2.2-2.2c.3-.3.7-.4 1-.2 1.1.4 2.3.6 3.6.6.6 0 1 .4 1 1V20c0 .6-.4 1-1 1A17 17 0 0 1 3 4c0-.6.4-1 1-1h3.5c.6 0 1 .4 1 1 0 1.3.2 2.5.6 3.6.1.3 0 .7-.2 1z"/></svg>
      <span>04 00 555 018</span>
    </div>
    <div class="contact">
      <svg viewBox="0 0 24 24"><path d="M2 5h20v14H2z M3 6l9 7 9-7" fill="none" stroke="#fff" stroke-width="2"/></svg>
      <span>office@harbourlineplumbing.example</span>
    </div>
    <div>ABN 00 000 000 000</div>
    <div>If compressor location cannot be back to back with head unit installation cost will be quoted onsite</div>
  </div>
</div>
</body>
</html>
```